Business card design for Velvet Harbor

We need business cards designed for our new marketing consulting company, Velvet Harbor. Our services include marketing strategy, go-to-market and launch planning, growth strategy, and execution. We serve medical technology and health technology companies, from startups to well-established growth companies.

The business cards should feel professional, credible, reliable and trustworthy, and should instill confidence. Also bold, creative, and modern.

The design must use the Velvet Harbor logo.

The primary brand color is this orange: #FF5501
A secondary color that you can use is this gray: #282B2D
I would prefer only to use the orange and gray. But if you feel you really need an additional accent color (please use it very sparingly, as little as possible), you can use this blue for small accent purposes: #009FED

Attached are the logo files. The main logo is the one with a little bit of orange on the left and the rest is gray.

The business card should include the following:

Velvet Harbor logo
First name and last name
Title
Email address
Phone number and type (in whatever order looks best for the design
Website (the website does not need to be in the same block as the personal info)

For example:

Nessa Pryle
Founder & Principal
nessa@velvetharbor.com
+1.628.309.4156 mobile (can use "." or spaces in between blocks of numbers)
velvetharbor.com (somewhere on the card, it does not need to be with the personal info; and note that there is no "www." at the beginning)

Note that there will be no address listed on the business card.

Target Market(s)

Executives (CEO, head of marketing, head of sales) at medical technology and health technology companies, mostly in their 40s and older, well-educated, often with advanced degrees. They are strategic thinkers, responsible for budgets, and familiar with P&L. Their comfort with and trust in using outside consultants varies.

Industry/Entity Type

Medical technology and health technology companies.

Contact Information for Business Card

See project description

Font styles to use
Sans Serif

Requirements
Must have
• Logo and see Business card details section above.

```html
<!DOCTYPE html>
<html lang="en">
<head>
<meta charset="utf-8">
<title>Velvet Harbor — Business Card</title>
<link rel="stylesheet" href="https://fonts.googleapis.com/css2?family=Montserrat:wght@300;400;700&display=swap">
<style>
  :root {
    --orange: #f15a22;
    --graphite: #282b2d;
    --paper: #ffffff;
    --muted: #d9d9d9;
  }
  * { margin: 0; padding: 0; box-sizing: border-box; }
  html, body { width: 1200px; height: 900px; overflow: hidden; background: var(--paper); }
  body { font-family: "Montserrat", sans-serif; position: relative; }

  .card {
    position: absolute;
    left: 285px;
    width: 630px;
    height: 360px;
    overflow: hidden;
    box-shadow: 0 6px 18px rgba(0,0,0,0.18);
  }
  .card--front { top: 65px; background: var(--orange); }
  .card--back { top: 475px; background: var(--graphite); }
  .card svg.shapes { position: absolute; inset: 0; }

  .wordmark {
    position: absolute;
    display: flex;
    align-items: center;
    gap: 14px;
    color: var(--graphite);
  }
  .wordmark__mark {
    width: 16px; height: 16px;
    background: var(--graphite);
    border-radius: 50%;
    flex: none;
  }
  .wordmark__name {
    font-weight: 400;
    font-size: 24px;
    line-height: 1.1;
    letter-spacing: 0.28em;
    text-transform: uppercase;
  }
  .card--front .wordmark { left: 320px; top: 140px; }
  .card--back .wordmark { left: 40px; top: 150px; }
  .card--back .wordmark__name { font-size: 20px; }

  .contact {
    position: absolute;
    left: 362px;
    top: 72px;
    color: var(--muted);
  }
  .contact__name {
    color: var(--orange);
    font-weight: 700;
    font-size: 32px;
    line-height: 1;
  }
  .contact__title {
    font-weight: 400;
    font-size: 14px;
    letter-spacing: 0.03em;
    margin-top: 6px;
  }
  .contact__rule {
    width: 66px; height: 2px;
    background: var(--orange);
    margin: 8px 0 22px;
  }
  .contact__list { list-style: none; }
  .contact__item {
    display: flex;
    align-items: center;
    gap: 12px;
    font-weight: 300;
    font-size: 16px;
    letter-spacing: 0.02em;
    margin-bottom: 12px;
  }
  .contact__icon { width: 20px; height: 20px; flex: none; }
</style>
</head>
<body>

<section class="card card--front" aria-label="Card front">
  <svg class="shapes" width="630" height="360" viewBox="0 0 630 360" aria-hidden="true">
    <circle cx="40" cy="360" r="300" fill="var(--graphite)"/>
    <circle cx="40" cy="360" r="215" fill="var(--orange)"/>
  </svg>
  <div class="wordmark">
    <span class="wordmark__mark"></span>
    <span class="wordmark__name">Velvet<br>Harbor</span>
  </div>
</section>

<section class="card card--back" aria-label="Card back">
  <svg class="shapes" width="630" height="360" viewBox="0 0 630 360" aria-hidden="true">
    <circle cx="30" cy="220" r="280" fill="var(--orange)"/>
    <circle class="dotted-edge" cx="30" cy="220" r="270" fill="none" stroke="var(--graphite)" stroke-width="4" stroke-dasharray="0.1 11" stroke-linecap="round"/>
  </svg>
  <div class="wordmark">
    <span class="wordmark__mark"></span>
    <span class="wordmark__name">Velvet<br>Harbor</span>
  </div>

  <div class="contact">
    <h1 class="contact__name">Nessa Pryle</h1>
    <p class="contact__title">Founder &amp; Principal</p>
    <div class="contact__rule"></div>
    <ul class="contact__list">
      <li class="contact__item">
        <svg class="contact__icon" viewBox="0 0 20 20" aria-hidden="true">
          <circle cx="10" cy="10" r="10" fill="var(--orange)"/>
          <path d="M6.5 5.5l2 0 1 2.5-1.2 1a6 6 0 0 0 2.7 2.7l1-1.2 2.5 1v2a1 1 0 0 1-1 1A8 8 0 0 1 5.5 6.5a1 1 0 0 1 1-1z" fill="var(--graphite)"/>
        </svg>
        +1 628 309 4156
      </li>
      <li class="contact__item">
        <svg class="contact__icon" viewBox="0 0 20 20" aria-hidden="true">
          <circle cx="10" cy="10" r="10" fill="var(--orange)"/>
          <rect x="5" y="6.5" width="10" height="7" rx="1" fill="none" stroke="var(--graphite)" stroke-width="1.4"/>
          <path d="M5.5 7l4.5 3.5L14.5 7" fill="none" stroke="var(--graphite)" stroke-width="1.4"/>
        </svg>
        nessa@velvetharbor.com
      </li>
      <li class="contact__item">
        <svg class="contact__icon" viewBox="0 0 20 20" aria-hidden="true">
          <path d="M10 2L1 10h3v8h4.5v-5h3v5H16v-8h3z" fill="var(--orange)"/>
        </svg>
        velvetharbor.com
      </li>
    </ul>
  </div>
</section>

</body>
</html>
```